WP website design (Durham)

We need a wordpress design that will incorporate a professional color scheme with company logo in a clean layout. The design needs to consider that this will be developed on a responsive theme. Colors are undetermined - subdued or subtle, perhaps earth tones colors will likely work well. Logo color can be changed from black to any other to suit.

Client wants a unique look for their site - mentions liking http://www.rtvole.com/ and http://www.brunsikeauction.com/. Possible but not necessary to have large slideshow element.

Industry/Entity Type

It Company

Font styles to use
Serif
Sans Serif

Colors

Designer to choose colors to be used in the design.

Requirements
Must have
• Navigation: 1)Home 2) Auctions 3) For Sale 4) Buyers & Sellers 5) Brokerage 6) About Us 7) Contact Us

Site will have slideshow, please use high-end stock real estate image initially. Header will have logo. Social icons (Facebook, Twitter, Youtube) and tagline "THE REAL ESTATE AUCTION AUTHORITY SINCE 1977" will be used.

Widgets Include: Email signup form, Featured Auctions, News & Events Blog, Featured Video widget.

Footer will have contact info (below), site navigation, smaller company logo, testimonial widget, affiliation logos (attached).
Nice to have
• Site will have drop-down menus - please indicate the styling, for instance the dropdown menus 1) Referrals 2) Properties For Sale under the 'Brokerage' link

```html
<!DOCTYPE html>
<html lang="en">
<head>
<meta charset="utf-8">
<title>R.Whitmore &amp; Associates</title>
<link href="https://fonts.googleapis.com/css2?family=Tinos:wght@400;700&family=Arimo:wght@400;700&display=swap" rel="stylesheet">
<style>
:root{
  --red:#c8202f;
  --ink:#222;
  --grey-band:#e3e3e3;
  --footer:#3a3a3a;
  --footer-bar:#2b2b2b;
  --line:#d8d8d8;
  --white:#fff;
}
*{box-sizing:border-box;margin:0;padding:0}
html,body{width:803px;height:1200px;overflow:hidden;background:var(--white)}
body{position:relative;font-family:"Arimo",Arial,sans-serif;color:var(--ink)}
.abs{position:absolute}

/* header */
.brand{left:68px;top:34px;font-family:"Tinos",serif;font-size:25px;line-height:30px;color:#1d1d1d;white-space:nowrap}
.follow{left:557px;top:37px;display:flex;align-items:center;gap:8px;font-size:16px;color:#333}
.follow .dot{width:24px;height:24px;border-radius:50%;background:#555;display:inline-block}
.follow .label{margin-right:6px}

/* nav */
.nav-rule{left:0;top:92px;width:803px;height:2px;background:var(--red)}
.nav{left:60px;top:97px;width:680px;height:20px;display:flex;align-items:center;font-family:"Tinos",serif;font-size:12px;color:#222}
.nav a{flex:1;text-align:center;border-left:1px solid #ccc;line-height:16px;white-space:nowrap}
.nav a:first-child{border-left:none}
.nav-caret{left:477px;top:94px;width:0;height:0;border-left:4px solid transparent;border-right:4px solid transparent;border-top:4px solid var(--red)}

/* hero */
.hero-band{left:0;top:120px;width:803px;height:312px;background:var(--red)}
.hero-frame{left:67px;top:139px;width:669px;height:273px;background:var(--white);padding:4px}
.hero-photo{width:100%;height:100%;background:linear-gradient(180deg,#5d7a45 0%,#8a5a42 40%,#9a5e47 65%,#6f8a43 100%)}
.hero-caption{left:85px;top:320px;width:497px;height:32px;background:rgba(30,30,30,.7);color:#fff;font-family:"Tinos",serif;font-size:17px;line-height:32px;padding-left:20px;white-space:nowrap}

/* dropdown */
.dropdown{left:415px;top:130px;width:138px;height:70px;background:rgba(225,225,225,.92);padding:15px 6px 0}
.dropdown .item{height:20px;border-radius:3px;font-size:8px;color:#fff;line-height:20px;padding-left:14px;position:relative;margin-bottom:5px;white-space:nowrap}
.dropdown .item::before{content:"";position:absolute;left:7px;top:7px;border-top:3px solid transparent;border-bottom:3px solid transparent;border-left:3px solid #fff}
.dropdown .on{background:var(--red)}
.dropdown .off{background:#3d3d3d}

/* welcome */
.welcome-title{left:0;top:448px;width:803px;text-align:center;font-family:"Tinos",serif;font-weight:700;font-size:21px;color:var(--red)}
.welcome-text{left:67px;top:484px;width:669px;text-align:center;font-size:9px;line-height:13.5px;color:#222}
.divider{left:67px;top:547px;width:669px;height:1px;background:var(--line)}
.section-title{left:0;top:563px;width:803px;text-align:center;font-family:"Tinos",serif;font-weight:700;font-size:15px;letter-spacing:.5px;color:var(--red)}

/* cards */
.card{top:601px;width:152px;height:179px;border:1px solid #d5d5d5;background:#fff}
.card-photo{position:absolute;left:7px;top:6px;width:137px;height:99px}
.card-title{position:absolute;top:111px;width:100%;text-align:center;font-weight:700;font-size:11px}
.card-text{position:absolute;top:128px;left:20px;right:20px;text-align:center;font-size:8.5px;line-height:11px;color:#444}
.card-foot{position:absolute;left:0;bottom:0;width:100%;height:22px;border-top:1px solid #ddd;font-size:9.5px;line-height:22px;padding-left:11px;white-space:nowrap}
.card-eye{position:absolute;right:0;top:0;width:20px;height:21px;background:var(--red);display:flex;align-items:center;justify-content:center}

/* widgets band */
.widgets{left:0;top:815px;width:803px;height:225px;background:var(--grey-band)}
.w-title{font-family:"Tinos",serif;font-weight:700;font-size:17px;color:var(--red);white-space:nowrap}
.col-rule{top:838px;width:1px;height:158px;background:#c9c9c9}
.signup-text{left:67px;top:870px;width:175px;font-size:8.5px;line-height:11px;color:#333}
.field{left:67px;width:165px;height:20px;background:#fff;border:1px solid #c4c4c4;font-size:9px;color:#888;line-height:18px;padding-left:6px}
.subscribe{left:67px;top:973px;width:91px;height:22px;border:2px solid #555;border-radius:11px;background:#f7f7f7;font-weight:700;font-size:9px;text-align:center;line-height:18px;color:#222}
.post{left:278px;width:236px;height:46px}
.date{position:absolute;left:0;top:0;width:40px;height:46px;background:#fff;border-radius:6px;text-align:center;box-shadow:0 0 0 1px #d2d2d2}
.date b{display:block;font-size:17px;margin-top:5px;line-height:18px}
.date span{font-size:10px}
.post-title{position:absolute;left:52px;top:3px;font-size:10px;color:var(--red);white-space:nowrap}
.post-text{position:absolute;left:52px;top:17px;width:176px;font-size:9px;line-height:13.5px;color:#555}
.post-more{position:absolute;left:182px;top:34px;font-size:8px;font-style:italic;color:var(--red);white-space:nowrap}
.video{left:545px;top:870px;width:191px;height:125px;background:radial-gradient(circle at 50% 40%,#3a3a3a,#111 75%);border:1px solid #000}
.video-bar{position:absolute;left:4px;right:4px;bottom:4px;height:12px;background:#2a2a2a;border:1px solid #4a4a4a}

/* footer */
.footer{left:0;top:1040px;width:803px;height:132px;background:var(--footer);color:#ddd}
.f-title{font-weight:700;font-size:15px;color:#fff}
.f-text{font-size:8.5px;line-height:13.5px;color:#ddd}
.f-brand{left:540px;top:1060px;width:200px;text-align:center;font-family:"Tinos",serif;font-size:17px;color:#fff;white-space:nowrap}
.badge{top:1108px;height:22px;background:#e8e8e8}
.bottom-nav{left:0;top:1172px;width:803px;height:28px;background:var(--footer-bar);display:flex;justify-content:center;align-items:center;font-size:9.5px;color:#fff}
.bottom-nav span{padding:0 15px}
.bottom-nav i{font-style:normal;color:#ccc}
</style>
</head>
<body>

<header>
  <div class="abs brand">R.Whitmore &amp; Associates</div>
  <div class="abs follow">
    <span class="label">Follow Us:</span>
    <span class="dot" aria-label="Social link 1"></span>
    <span class="dot" aria-label="Social link 2"></span>
    <span class="dot" aria-label="Social link 3"></span>
  </div>
</header>

<div class="abs nav-rule"></div>
<div class="abs nav-caret"></div>
<nav class="abs nav">
  <a>Home</a><a>Auctions</a><a>For Sale</a><a>Buyers &amp; Sellers</a><a>Brokerage</a><a>About Us</a><a>Contact Us</a>
</nav>

<section>
  <div class="abs hero-band"></div>
  <div class="abs hero-frame">
    <div class="hero-photo" role="img" aria-label="Red brick two-storey family home with white trim, lawn and flower beds"></div>
  </div>
  <div class="abs hero-caption">THE REAL ESTATE AUCTION AUTHORITY SINCE 1977</div>
  <div class="abs dropdown">
    <div class="item on">Referrals</div>
    <div class="item off">Properties For Sale</div>
  </div>
</section>

<section>
  <h1 class="abs welcome-title">Welcome R.Whitmore</h1>
  <p class="abs welcome-text">Lorem ipsum dolor sit amet, consectetur adipisicing elit, sed do eiusmod tempor incididunt ut labore et dolore magna aliqua. Ut enim ad minim veniam, quis nostrud exercitation ullamco laboris nisi ut aliquip ex ea commodo consequat. Duis aute irure dolor in reprehenderit in voluptate velit esse cillum dolore eu fugiat nulla pariatur. Excepteur sint occaecat cupidatat non proident, sunt in culpa qui officia deserunt mollit anim id est laborum...</p>
  <div class="abs divider"></div>
  <h2 class="abs section-title">FEATURED AUCTIONS</h2>

  <div class="abs card" style="left:68px">
    <div class="card-photo" role="img" aria-label="Craftsman style house with stone accents" style="background:linear-gradient(180deg,#8fb6d8 0%,#7d7458 50%,#6b7a3d 100%)"></div>
    <div class="card-title">Lorem ipsum</div>
    <div class="card-text">dolor sit amet, consectetur adipiscing elit</div>
    <div class="card-foot">04/09/14 to 05/09/14<span class="card-eye"><svg width="12" height="8" viewBox="0 0 12 8"><path d="M1 4 Q6 -1 11 4 Q6 9 1 4Z" fill="none" stroke="#fff" stroke-width="1.3"/><circle cx="6" cy="4" r="1.6" fill="#fff"/></svg></span></div>
  </div>
  <div class="abs card" style="left:240px">
    <div class="card-photo" role="img" aria-label="Grey two-storey house under blue sky" style="background:linear-gradient(180deg,#2f62b8 0%,#9aa3ad 50%,#4f8a2c 100%)"></div>
    <div class="card-title">Lorem ipsum</div>
    <div class="card-text">dolor sit amet, consectetur adipiscing elit</div>
    <div class="card-foot">04/09/14 to 05/09/14<span class="card-eye"><svg width="12" height="8" viewBox="0 0 12 8"><path d="M1 4 Q6 -1 11 4 Q6 9 1 4Z" fill="none" stroke="#fff" stroke-width="1.3"/><circle cx="6" cy="4" r="1.6" fill="#fff"/></svg></span></div>
  </div>
  <div class="abs card" style="left:412px">
    <div class="card-photo" role="img" aria-label="Stone and stucco house with garden" style="background:linear-gradient(180deg,#7fa2c4 0%,#b8a58a 50%,#6b6a3e 100%)"></div>
    <div class="card-title">Lorem ipsum</div>
    <div class="card-text">dolor sit amet, consectetur adipiscing elit</div>
    <div class="card-foot">04/09/14 to 05/09/14<span class="card-eye"><svg width="12" height="8" viewBox="0 0 12 8"><path d="M1 4 Q6 -1 11 4 Q6 9 1 4Z" fill="none" stroke="#fff" stroke-width="1.3"/><circle cx="6" cy="4" r="1.6" fill="#fff"/></svg></span></div>
  </div>
  <div class="abs card" style="left:584px">
    <div class="card-photo" role="img" aria-label="White house with porch and red shutters" style="background:linear-gradient(180deg,#9bb8cf 0%,#d8d5cf 50%,#5f7a3a 100%)"></div>
    <div class="card-title">Lorem ipsum</div>
    <div class="card-text">dolor sit amet, consectetur adipiscing elit</div>
    <div class="card-foot">04/09/14 to 05/09/14<span class="card-eye"><svg width="12" height="8" viewBox="0 0 12 8"><path d="M1 4 Q6 -1 11 4 Q6 9 1 4Z" fill="none" stroke="#fff" stroke-width="1.3"/><circle cx="6" cy="4" r="1.6" fill="#fff"/></svg></span></div>
  </div>
</section>

<section>
  <div class="abs widgets"></div>
  <div class="abs col-rule" style="left:257px"></div>
  <div class="abs col-rule" style="left:526px"></div>

  <h3 class="abs w-title" style="left:67px;top:835px">Email Sign Up</h3>
  <p class="abs signup-text">Lorem ipsum dolor sit amet, consectetuer adipiscing elit. Nam</p>
  <div class="abs field" style="top:905px">Your Name</div>
  <div class="abs field" style="top:939px">Email Address</div>
  <div class="abs subscribe">Subscribe Now</div>

  <h3 class="abs w-title" style="left:286px;top:835px">News &amp; Event Blog</h3>
  <div class="abs post" style="top:873px">
    <div class="date"><b>25</b><span>Dec</span></div>
    <div class="post-title">Lorem ipsum dolor sit amet</div>
    <div class="post-text">Lorem ipsum dolor sit amet, consectetur<br>adipiscing elit labore aliqua.</div>
    <div class="post-more">Read More...</div>
  </div>
  <div class="abs post" style="top:940px">
    <div class="date"><b>25</b><span>Dec</span></div>
    <div class="post-title">Lorem ipsum dolor sit amet</div>
    <div class="post-text">Lorem ipsum dolor sit amet, consectetur<br>adipiscing elit labore aliqua.</div>
    <div class="post-more">Read More...</div>
  </div>

  <h3 class="abs w-title" style="left:545px;top:835px">Featured Video</h3>
  <div class="abs video" role="img" aria-label="Company introduction video">
    <svg class="abs" style="left:78px;top:38px" width="34" height="30" viewBox="0 0 34 30"><rect width="34" height="30" rx="3" fill="rgba(0,0,0,.6)"/><path d="M12 7 L25 15 L12 23Z" fill="#fff"/></svg>
    <div class="video-bar">
      <svg width="181" height="10" viewBox="0 0 181 10"><path d="M4 2 L9 5 L4 8Z" fill="#fff"/><text x="20" y="8" font-size="6" fill="#fff" font-family="Arimo,sans-serif">00:00</text><rect x="42" y="4" width="98" height="2" fill="#888"/><text x="146" y="8" font-size="6" fill="#fff" font-family="Arimo,sans-serif">00:00</text><rect x="166" y="3" width="10" height="4" fill="#aaa"/></svg>
    </div>
  </div>
</section>

<footer>
  <div class="abs footer"></div>
  <h4 class="abs f-title" style="left:74px;top:1052px">Contact Us</h4>
  <p class="abs f-text" style="left:74px;top:1077px">R.Whitmore Estate And Auction Co<br>P.O. Box 52, Fairlake, MN 55810<br>Phone (Office): 800-555-0142<br>Phone (Fax): 507-555-0187</p>

  <h4 class="abs f-title" style="left:287px;top:1052px">Testimonials</h4>
  <div class="abs" style="left:281px;top:1066px;font-family:'Tinos',serif;font-size:20px;color:#999">&ldquo;</div>
  <p class="abs f-text" style="left:294px;top:1075px;width:190px;line-height:12px">Lorem ipsum dolor sit amet, consectetur adipi-scing elit, sed do eiusmod tempor incididunt ut labore et dolore magna aliqua. Ut enim ad minim veniam, Excepteur sint occaecat cupidatat non proident, sunt in culpa qui officia deserunt mollit anim id est laborum.</p>

  <div class="abs f-brand">R.Whitmore &amp; Associates</div>
  <div class="abs badge" style="left:556px;width:22px" aria-label="Affiliation badge"></div>
  <div class="abs badge" style="left:586px;width:28px;border-radius:3px" aria-label="Affiliation badge"></div>
  <div class="abs badge" style="left:620px;width:20px" aria-label="Affiliation badge"></div>
  <div class="abs badge" style="left:646px;width:42px;border-radius:11px" aria-label="Affiliation badge"></div>
  <div class="abs badge" style="left:696px;width:26px;border-radius:50%" aria-label="Affiliation badge"></div>
  <p class="abs f-text" style="left:544px;top:1145px;color:#fff;white-space:nowrap">Copyright (C) R.whitmore. 2013.  All Rights Reserved</p>

  <nav class="abs bottom-nav">
    <span>Home</span><i>|</i><span>Auctions</span><i>|</i><span>For Sale</span><i>|</i><span>Buyers &amp; Sellers</span><i>|</i><span>Brokerage</span><i>|</i><span>About Us</span><i>|</i><span>Contact Us</span>
  </nav>
</footer>

</body>
</html>
```